Admin Backend Redesign

We need a redesign for our backend which supoosed to make the backoffice look more modern!

I will add screenshots of the backoffice so you know what data will be shown in the Admin.

Have in mind that the users of this backend are Doctors. We need a clinical look, modern and sharp. The backoffice is responsive, have that in mind. We need the backoffice to look as professional as possible.

The theme used for the website is: http://velmora.quillstack-sample.com/

ON the main page of the backoffice, under every widget i need some space to write an explanation what the widget is about.

The color code used in our logo and website is #57aad4 combined with white.

We are open for ideas!
Updates

Project Deadline Extended
Reason: Designs are ok, but nothing innovative. Please use more modern designs!

Project Deadline Extended
Reason: Havent recieved a perfect design yet. Please read instructions carefully! Thank you

Project Deadline Extended
Reason: Hey everybody, sorry for the delay. We will decide in 3 days. If anyone wants to add a Design, that would be great.

Target Market(s)

Doctors, therapists

Industry/Entity Type

It Professional

Font styles to use
Sans Serif

Requirements
Must have
• Must look uptodate, modern, like new back offices look nowadays

```html
<!DOCTYPE html>
<html lang="en">
<head>
<meta charset="utf-8">
<title>AdminBackend – Dashboard</title>
<link href="https://fonts.googleapis.com/css2?family=Open+Sans:wght@300;400;600;700&family=Roboto:wght@400;500&display=swap" rel="stylesheet">
<style>
:root{
  --blue:#1e88f5;
  --blue-light:#2ec8fb;
  --sky:#57aad4;
  --ink:#3c4752;
  --ink-soft:#5f6b75;
  --label:#5b5753;
  --muted:#9aa4ac;
  --line:#e3e6ea;
  --field:#f7f8f9;
  --topbar:#f5f8fc;
  --crumb:#f4f5f6;
  --date:#c2cbd2;
  --red:#f0675c;
  --green:#8cc152;
  --orange:#f5a623;
  --placeholder-a:#eef5fc;
  --placeholder-b:#cfe2f5;
  --white:#ffffff;
}
*{box-sizing:border-box;margin:0;padding:0}
html,body{width:1200px;height:654px;overflow:hidden;background:var(--white);font-family:"Open Sans",Arial,sans-serif;color:var(--ink)}
.canvas{position:relative;width:1200px;height:654px}
.abs{position:absolute}

/* top bar */
.topbar{left:0;top:0;width:1200px;height:65px;background:var(--topbar)}
.tool-icon{width:26px;height:24px;border:1px solid #d4d9de;border-radius:3px;background:var(--white);top:23px;display:flex;align-items:center;justify-content:center}
.count{position:absolute;top:-10px;right:-7px;width:17px;height:17px;border-radius:50%;color:#fff;font-size:10px;font-weight:700;display:flex;align-items:center;justify-content:center}
.count.green{background:var(--green)}.count.red{background:var(--red)}.count.orange{background:var(--orange)}
.divider{left:200px;top:14px;width:1px;height:38px;background:#dfe3e7}
.top-link{top:22px;font-size:14px;color:var(--ink-soft)}
.pill{display:inline-flex;align-items:center;justify-content:center;width:16px;height:16px;border-radius:50%;background:var(--red);color:#fff;font-size:10px;margin-left:2px;vertical-align:1px}
.avatar{left:1027px;top:13px;width:38px;height:38px;border-radius:50%;border:1px solid #cfd6dd;background:var(--white);display:flex;align-items:center;justify-content:center}

/* brand band */
.band{left:0;top:65px;width:1200px;height:50px;background:linear-gradient(90deg,var(--blue),var(--blue-light))}
.brand{left:62px;top:72px;font-size:26px;font-weight:700;color:#fff;letter-spacing:.2px}
.band-btn{top:71px;height:36px;border:1px solid rgba(255,255,255,.75);color:#fff;font-size:14px;display:flex;align-items:center;justify-content:center;gap:6px}

/* sidebar */
.start{left:59px;top:147px;width:188px;height:39px;background:#e9f5fd;border:1px solid #a9d5f2;font-size:13.5px;color:var(--ink-soft);display:flex;align-items:center;padding-left:20px;gap:6px}
.side-title{left:59px;top:203px;font-size:13px;color:#aab4bc;letter-spacing:.3px}
.nav{left:67px;font-size:13.5px;color:var(--ink-soft);display:flex;align-items:center;gap:7px}
.nav.active{color:#25a9e8}
.nav-badge{left:213px;top:271px;width:24px;height:15px;border-radius:8px;background:var(--red);color:#fff;font-size:10px;display:flex;align-items:center;justify-content:center}
.emblem-area{left:62px;top:386px;width:174px;height:166px;background:linear-gradient(160deg,var(--placeholder-a),var(--placeholder-b))}

/* main */
.welcome{left:271px;top:138px;font-size:29px;font-weight:300;color:var(--ink)}
.crumb{left:271px;top:189px;width:637px;height:33px;background:var(--crumb);display:flex;align-items:center;padding-left:10px;gap:8px;font-size:13.5px;color:var(--ink-soft)}
.date{left:908px;top:189px;width:231px;height:33px;background:var(--date);color:#fff;font-size:12.5px;display:flex;align-items:center;justify-content:center;gap:6px}

.panel{left:270px;top:243px;width:873px;height:340px;border:1px solid #2a9af7}
.panel-head{position:absolute;left:0;top:0;width:100%;height:42px;background:linear-gradient(90deg,var(--blue),var(--blue-light));display:flex;align-items:center;padding-left:20px;gap:12px;color:#fff;font-size:20px}
.label{position:absolute;font-family:Roboto,Arial,sans-serif;font-weight:500;font-size:13px;color:var(--label);text-align:center;transform:translateY(-50%)}
.field{position:absolute;height:34px;background:var(--field);border:1px solid var(--line)}
.select{font-size:13px;color:#a3a9ae;padding:9px 10px;font-family:Roboto,Arial,sans-serif}
.select::after{content:"";position:absolute;right:9px;top:14px;border:4px solid transparent;border-top:5px solid #777}
.check{position:absolute;top:246px;display:flex;align-items:center;gap:7px;font-family:Roboto,Arial,sans-serif;font-size:12.5px;color:#666}
.box{width:18px;height:18px;border:1px solid #8f9499;border-radius:2px;background:#fff}
.submit{position:absolute;left:678px;top:230px;width:186px;height:30px;background:var(--blue);color:#fff;font-size:13.5px;font-weight:500;white-space:nowrap;display:flex;align-items:center;justify-content:center}
.footer{left:67px;top:611px;font-size:11.5px;letter-spacing:1.6px;color:var(--ink)}
</style>
</head>
<body>
<div class="canvas">
  <div class="abs topbar"></div>
  <div class="abs tool-icon" style="left:68px"><svg width="14" height="11"><rect y="0" width="14" height="2.5" fill="#556"/><rect y="4.2" width="14" height="2.5" fill="#556"/><rect y="8.4" width="14" height="2.5" fill="#556"/></svg><span class="count green">6</span></div>
  <div class="abs tool-icon" style="left:108px"><svg width="15" height="11"><rect x=".5" y=".5" width="14" height="10" fill="none" stroke="#556"/><path d="M1 1l6.5 5L14 1" fill="none" stroke="#556"/></svg><span class="count red">5</span></div>
  <div class="abs tool-icon" style="left:149px"><svg width="14" height="15"><path d="M3 11V6a4 4 0 018 0v5l2 1.5H1z" fill="none" stroke="#556"/><circle cx="7" cy="13.5" r="1.3" fill="#556"/></svg><span class="count orange">7</span></div>
  <div class="abs divider"></div>
  <div class="abs top-link" style="left:219px">My Notifications<span class="pill">2</span></div>
  <div class="abs top-link" style="left:950px">Invites <span class="pill">2</span></div>
  <div class="abs avatar"><svg width="12" height="16"><rect x="2" y="1" width="8" height="9" rx="4" fill="none" stroke="#9aa4ac"/><path d="M1 15c1-3 9-3 10 0" fill="none" stroke="#9aa4ac"/></svg></div>
  <div class="abs top-link" style="left:1077px">Doctor</div>
  <svg class="abs" style="left:1130px;top:29px" width="10" height="6"><path d="M0 0h10L5 6z" fill="#9aa4ac"/></svg>

  <div class="abs band"></div>
  <div class="abs brand">AdminBackend</div>
  <div class="abs band-btn" style="left:857px;width:156px"><svg width="14" height="14"><rect x="1" y="3" width="8" height="10" fill="none" stroke="#fff" stroke-width="1.3"/><rect x="5" y="1" width="8" height="10" fill="none" stroke="#fff" stroke-width="1.3"/></svg>Recent Projects<svg width="9" height="5"><path d="M0 0h9L4.5 5z" fill="#fff"/></svg></div>
  <div class="abs band-btn" style="left:1020px;width:119px"><svg width="14" height="14"><path d="M7 0v14M0 7h14" stroke="#fff" stroke-width="1.6"/></svg>New project</div>

  <div class="abs start"><svg width="15" height="10"><path d="M4 9.5a3.5 3.5 0 010-7 4.5 4.5 0 018.5 1.5 3 3 0 01-1 5.5z" fill="none" stroke="#5f6b75"/></svg>Let's get started</div>
  <div class="abs side-title">GENERAL</div>
  <div class="abs nav active" style="top:235px"><svg width="14" height="14"><circle cx="7" cy="7" r="6" fill="none" stroke="#25a9e8" stroke-width="1.5"/><path d="M7 7l3-3" stroke="#25a9e8" stroke-width="1.5"/></svg>Dashboard / Projects</div>
  <div class="abs nav" style="top:269px"><svg width="14" height="14"><rect x="1" y="1" width="9" height="9" fill="none" stroke="#5f6b75"/><rect x="4" y="4" width="9" height="9" fill="#fff" stroke="#5f6b75"/></svg>Patients Reviews</div>
  <div class="abs nav-badge">23</div>
  <div class="abs nav" style="top:304px"><svg width="14" height="14"><rect x="1" y="1" width="12" height="12" fill="none" stroke="#5f6b75"/><path d="M1 4h12M4 7h1M7 7h1M10 7h1M4 10h1M7 10h1M10 10h1" stroke="#5f6b75"/></svg>Patient Details</div>
  <div class="abs emblem-area" role="img" aria-label="Medical emblem illustration in blue and white"></div>

  <div class="abs welcome">Welcome Dr.Halden Roe</div>
  <div class="abs crumb"><svg width="12" height="10"><path d="M6 0l6 5h-2v5H7V7H5v3H2V5H0z" fill="#7d8790"/></svg>Home <span style="color:#aaa">›</span> Dashboard</div>
  <div class="abs date"><svg width="12" height="12"><rect x=".5" y="1.5" width="11" height="10" fill="none" stroke="#fff"/><path d="M.5 4.5h11" stroke="#fff"/></svg>MAY 28, 2014 - JUNE 26, 2014 <svg width="8" height="5"><path d="M0 0l4 4 4-4" fill="none" stroke="#fff" stroke-width="1.4"/></svg></div>

  <section class="abs panel">
    <div class="panel-head"><svg width="19" height="19"><rect x="1" y="3" width="14" height="14" rx="2" fill="none" stroke="#fff" stroke-width="2"/><path d="M8 11l9-9" stroke="#fff" stroke-width="2.4"/></svg>Arzte Verwalten</div>

    <div class="label" style="left:44px;top:85px">Full Name *</div>
    <div class="field" style="left:187px;top:70px;width:220px"></div>
    <div class="label" style="left:42px;top:135px">Password Confirm *</div>
    <div class="field" style="left:186px;top:119px;width:220px"></div>
    <div class="label" style="left:43px;top:190px">Normal select box *</div>
    <div class="field select" style="left:184px;top:174px;width:225px">Please choose</div>
    <div class="label" style="left:44px;top:262px">Check at least 2<br>checkboxes *</div>
    <div class="check" style="left:181px"><span class="box"></span>Option 1</div>
    <div class="check" style="left:283px"><span class="box"></span>Option 2</div>
    <div class="check" style="left:396px"><span class="box"></span>Option 3</div>

    <div class="label" style="left:477px;top:75px">Password *</div>
    <div class="field" style="left:571px;top:60px;width:268px"></div>
    <div class="label" style="left:480px;top:134px">Website</div>
    <div class="field" style="left:571px;top:119px;width:268px"></div>
    <div class="label" style="left:484px;top:190px">Birthdate</div>
    <div class="field" style="left:571px;top:175px;width:268px"></div>
    <div class="submit">Neuen Patient Hinzfugen +</div>
  </section>

  <div class="abs footer">© 2014 All right.reserved</div>
</div>
</body>
</html>
```